Quenderil - Still Grace Cosmetics

Please design a logo and business cards for new food supplements, cosmetics and herbal fixatives. The products are produced ecologically and biologically in the South Tyrol and Trentino alps. The products are pure and noble. Quenderil = pure vitality Colors Background: dark or black matt (soft touch) Logodesign: powerful, elegant, violet with glossy foil The logo and design should convey warmth, passion and the 6th sense, you should get the impression that you can smell the herbal odor , Logo and business cards for new food supplements, cosmetics and herbal fixatives. The products are produced ecologically and biologically in the South Tyrol and Trentino alps. The products are pure and noble. Quenderil = pure vitality Colors Background: dark or black matt (softtouch) Logodesign: powerful elegant violet with glossy foil The logo and design is meant to convey warmth, passion and the 6th sense, you should get the impression that you can smell the herbal perfume.

Target Market(s)

Food, food supplements, vitality, health

Contact Information for Business Card

Please provide an elegant darf design that is puristic, but has a very good logo design
Elegantes dunkles design, puristisch

Logo Text

Quenderil - still Grace

Colors
6b449b

Requirements
Must have
• SVG Files Alpha channel for foil embossing High-quality design
Nice to have
• Pure elegance
Should not have
• to colorful colors

```html
<!DOCTYPE html>
<html lang="en">
<head>
<meta charset="utf-8">
<title>Quenderil – Business Cards</title>
<link rel="stylesheet" href="https://fonts.googleapis.com/css2?family=Open+Sans:wght@400;600&display=swap">
<style>
  :root {
    --canvas: #3a3a3a;
    --card: #121212;
    --card-edge: #1e1e1e;
    --accent: #6b449b;
    --accent-text: #9670c8;
    --text: #e6e6e6;
    --muted: #a8a8a8;
    --divider: #2a2a2a;
  }
  * { margin: 0; padding: 0; box-sizing: border-box; }
  html, body {
    width: 1200px; height: 900px; overflow: hidden;
    background: var(--canvas);
    font-family: "Open Sans", Arial, sans-serif;
  }
  .sheet {
    position: relative; width: 1200px; height: 900px;
    display: flex; align-items: center; justify-content: center; gap: 50px;
  }
  .card {
    width: 500px; height: 290px;
    background: var(--card);
    border: 1px solid var(--card-edge);
    border-radius: 18px;
    position: relative;
    overflow: hidden;
  }
  /* contact side */
  .card-contact { display: flex; }
  .brand-panel {
    width: 52%;
    display: flex; align-items: center; justify-content: center; gap: 12px;
    border-right: 1px solid var(--divider);
    margin: 40px 0;
  }
  .brand-dot {
    width: 22px; height: 22px; border-radius: 50%;
    background: var(--accent);
  }
  .brand-name {
    color: var(--accent-text); font-size: 30px; font-weight: 600; letter-spacing: 1px;
  }
  .details {
    flex: 1; padding: 62px 0 0 26px; color: var(--text);
  }
  .person-name { color: var(--accent-text); font-size: 19px; font-weight: 400; line-height: 1.1; }
  .person-role { font-size: 12px; margin-bottom: 12px; }
  .address { font-size: 12.5px; line-height: 1.35; margin-bottom: 12px; }
  .contact-list { list-style: none; font-size: 12.5px; line-height: 1.5; }
  .contact-list li { display: flex; align-items: center; gap: 8px; }
  .contact-list svg { width: 11px; height: 11px; flex: none; color: var(--accent-text); }
  /* logo side */
  .card-brand {
    display: flex; flex-direction: column; align-items: center; justify-content: center; gap: 14px;
  }
  .card-brand .brand-dot { width: 28px; height: 28px; }
  .card-brand .brand-name {
    color: var(--muted); font-size: 38px; font-weight: 400; letter-spacing: 6px; text-transform: uppercase;
  }
</style>
</head>
<body>
<main class="sheet">
  <section class="card card-contact" aria-label="Business card, contact side">
    <div class="brand-panel">
      <span class="brand-dot" aria-hidden="true"></span>
      <span class="brand-name">Quenderil</span>
    </div>
    <div class="details">
      <h1 class="person-name">Elias Marrow</h1>
      <p class="person-role">Managing Director</p>
      <p class="address">12345, Address Goes Here<br>Country Name, 123456.</p>
      <ul class="contact-list">
        <li>
          <svg viewBox="0 0 12 12" aria-hidden="true"><path fill="currentColor" d="M2.5 1l2 2.2-1 1.3a7 7 0 0 0 4 4l1.3-1 2.2 2-1.2 1.5C5 10.8 1.2 7 .9 2.2z"/></svg>
          044-987 654 321
        </li>
        <li>
          <svg viewBox="0 0 12 12" aria-hidden="true"><rect x="0.5" y="2" width="11" height="8" fill="currentColor"/><path d="M0.5 2.3L6 6.5l5.5-4.2" fill="none" stroke="#121212" stroke-width="1"/></svg>
          hello@quenderil.com
        </li>
        <li>
          <svg viewBox="0 0 12 12" aria-hidden="true"><g fill="none" stroke="currentColor" stroke-width="1.6"><rect x="1" y="5" width="6" height="3.5" rx="1.7" transform="rotate(-45 4 6.75)"/><rect x="5" y="3.5" width="6" height="3.5" rx="1.7" transform="rotate(-45 8 5.25)"/></g></svg>
          www.quenderil.com
        </li>
      </ul>
    </div>
  </section>

  <section class="card card-brand" aria-label="Business card, logo side">
    <span class="brand-dot" aria-hidden="true"></span>
    <span class="brand-name">Quenderil</span>
  </section>
</main>
</body>
</html>
```